Tax Firm - Creative Print Ads to Build New Clients

I'm the marketing director of an integrated financial services business based in Melbourne Australia. I need to create a series of 4 press ads to run in the local business newspaper.

Each ad needs to stand alone, but at the same time should appear visually as from the same company and be part of a series.

The ad will will 115mm by 255mm (1/3 of a page horizontal)

Final artwork needs to be setup using CMYK and at the exact dimensions no bleed.

Brief
- Our tax practice provides services to individuals & small businesses (cafes, tradespeoeple, retailers)
- Our tagline is Bold, Proactive, Strategic, Practical financial advice, Where Futures Settle (a brand logo will be provided)
- The company logo needs to be included
- Web address included
- phone number included
- The ad needs to be professional, yet energetic
- Stock photography should be at an absolute minimum where models are not identifable
- Graphics are prefered over stock images
- Sketches are great
- Key message - we do tax returns, we care about you as an individual, we've been in the Docklands for 20 years, we are your local partner in your financial journey
Updates

Target Market(s)

Individuals earning between 50,000 and 200,000 per annum

Industry/Entity Type

Accounting

Font styles to use
Sans Serif
Script

Colors
3176b5
1b1b1b
fbf289
ec1f27
85acd3
0355a3

Requirements
Must have
• Sell t services to individuals as primary audience, with small businesses as a secondary audience.
• ---- Updated ----
• The company is www.velmorbay.com.au
• I've added
• - logos (vertical, horizontal, reverse and our brand tagline too)
• - Brand Guidelines
Nice to have
• I want to see some graphics that sell the idea that we are a local firm with 20 years experience in the area.
• We care about individuals first
Should not have
• Avoid using stock images where the pretty model is identifiable, we hate to see actors in our ads

```html
<!DOCTYPE html>
<html lang="en">
<head>
<meta charset="utf-8">
<title>Velmorbay – Press Ad</title>
<link rel="stylesheet" href="https://fonts.googleapis.com/css2?family=Fira+Sans:ital,wght@0,300;0,400;0,500;1,400&family=Oswald:wght@500&family=Dancing+Script:wght@500&display=swap">
<style>
  :root {
    --ink: #1b1b1b;
    --ink-soft: #2e2e2e;
    --red: #ec1f27;
    --paper: #f4f4f4;
    --paper-shade: #dcdcdc;
    --text: #222222;
    --white: #ffffff;
    --backdrop: #e9e9e9;
    --photo-light: #d9dde2;
    --photo-mid: #a9b2bc;
    --photo-blue: #3176b5;
  }
  * { margin: 0; padding: 0; box-sizing: border-box; }
  html, body {
    width: 1200px; height: 825px; overflow: hidden;
    background: var(--backdrop);
  }
  .ad {
    position: absolute; left: 50px; top: 165px;
    width: 1100px; height: 496px;
    background: linear-gradient(180deg, var(--white) 0%, var(--paper) 55%, var(--paper-shade) 100%);
    font-family: "Fira Sans", sans-serif;
    color: var(--text);
    overflow: hidden;
    box-shadow: 0 6px 18px rgba(0,0,0,.18);
  }
  .ad__header {
    position: absolute; left: 0; top: 0; width: 600px; height: 128px;
    background: linear-gradient(180deg, var(--ink-soft) 0%, var(--ink) 100%);
  }
  .ad__header-rule {
    position: absolute; left: 0; top: 128px; width: 600px; height: 14px;
    background: var(--red);
  }
  .brand {
    position: absolute; left: 46px; top: 36px;
    display: flex; align-items: center; gap: 22px;
  }
  .brand__dot {
    width: 52px; height: 52px; border-radius: 50%; background: var(--white);
  }
  .brand__name {
    font-weight: 300; font-size: 40px; letter-spacing: 7px; color: var(--white);
  }
  .ad__visual { position: absolute; left: 0; top: 0; width: 1100px; height: 340px; }
  .services {
    position: absolute; left: 38px; top: 186px;
    display: grid; grid-template-columns: 274px 230px; column-gap: 0;
    list-style: none;
    font-style: italic; font-size: 16.5px; line-height: 21px;
  }
  .services li { position: relative; padding-left: 16px; white-space: nowrap; }
  .services li.bullet::before {
    content: ""; position: absolute; left: 0; top: 7px;
    width: 8px; height: 8px; border-radius: 50%; background: var(--red);
  }
  .call {
    position: absolute; left: 30px; top: 292px; width: 448px; height: 94px;
    border: 4px solid var(--red); border-radius: 24px;
    background: var(--white);
    display: flex; align-items: center; justify-content: center; gap: 14px;
    font-family: "Oswald", sans-serif; font-weight: 500; font-size: 54px;
    box-shadow: 0 4px 8px rgba(0,0,0,.12);
  }
  .call__label { color: var(--red); }
  .call__number { color: var(--ink); }
  .web {
    position: absolute; left: 75px; top: 404px;
    font-size: 21px; font-weight: 500; letter-spacing: 3px; color: var(--ink);
  }
  .values {
    position: absolute; left: 500px; top: 373px;
    font-size: 19px; font-weight: 500; letter-spacing: 3.4px; word-spacing: 10px;
    color: var(--ink);
  }
  .tagline {
    position: absolute; right: 38px; top: 406px;
    font-family: "Dancing Script", cursive; font-size: 22px; color: var(--ink-soft);
  }
  .ad__footer {
    position: absolute; left: 0; top: 454px; width: 1100px; height: 42px;
    background: var(--ink);
  }
  .ad__footer-bar {
    position: absolute; left: 139px; top: 8px; width: 828px; height: 34px;
    background: var(--red);
  }
</style>
</head>
<body>
  <main class="ad">
    <div class="ad__header"></div>
    <div class="ad__header-rule"></div>

    <svg class="ad__visual" width="1100" height="340" viewBox="0 0 1100 340">
      <defs>
        <linearGradient id="photoTone" x1="0" y1="0" x2="1" y2="1">
          <stop offset="0" stop-color="var(--photo-light)"/>
          <stop offset="0.55" stop-color="var(--photo-mid)"/>
          <stop offset="1" stop-color="var(--photo-blue)" stop-opacity="0.7"/>
        </linearGradient>
      </defs>
      <polygon points="560,0 1100,0 1100,323 541,323" fill="var(--red)"/>
      <polygon class="ad__photo" role="img" aria-label="Photo: hands typing on a laptop beside a printed report with blue bar and pie charts" points="572,0 1100,0 1100,323 553,323" fill="url(#photoTone)"/>
      <rect x="541" y="323" width="559" height="14" fill="var(--red)"/>
    </svg>

    <div class="brand">
      <span class="brand__dot"></span>
      <span class="brand__name">VELMORBAY</span>
    </div>

    <ul class="services">
      <li class="bullet">Accounting and Business Advice</li>
      <li class="bullet">Property Sales and Leasing</li>
      <li class="bullet">Tax &amp; Audit</li>
      <li class="bullet">Property Insights and</li>
      <li class="bullet">Finance Brokering</li>
      <li class="bullet">Advisory</li>
      <li class="bullet">Legal &amp; Financial Planning</li>
      <li class="bullet">Property Investment</li>
    </ul>

    <div class="call">
      <span class="call__label">CALL:</span>
      <span class="call__number">03 9555 0142</span>
    </div>
    <p class="web">www.velmorbay.com.au</p>

    <p class="values">BOLD PROACTIVE STRATEGIC PRACTICAL</p>
    <p class="tagline">Where Futures Settle</p>

    <div class="ad__footer"><div class="ad__footer-bar"></div></div>
  </main>
</body>
</html>
```